Velvet Harbor for sale at the 2019 Tandor Crest Mare Auction on 30 May 2019

I am selling my broodmare at the 2019 Tandor Crest Mare auction on 30 May 2019. I need a flyer to hand out to potential buyers. I have included the required information in the attached word document. I can provide more images if required. I am thinking that a DL double sided or an A5 will suit best. I'm happy to provide more information as required.

Target Market(s)

Race horse breeders, people who buy broodmares.

Font styles to use
Serif
Sans Serif
Script

Colors

Designer to choose colors to be used in the design.

Requirements
Must have
• All of the content provided in the attached brief, however it is not necessary to have the words exactly as per the brief. The brief is for information purposes.
Nice to have
• Innovation...

```html
<!DOCTYPE html>
<html lang="en">
<head>
<meta charset="utf-8">
<title>Velvet Harbor – Tandor Crest Mare Auction Flyer</title>
<link rel="stylesheet" href="https://fonts.googleapis.com/css2?family=Allerta+Stencil&family=Open+Sans:wght@400&family=Roboto+Condensed:wght@300;400&display=swap">
<style>
  :root {
    --board: #464646;
    --paper: #ffffff;
    --brand-red: #d9434f;
    --ink: #2b2b2b;
    --label: #1e1e1e;
    --grass-light: #7fae3a;
    --grass-dark: #4e7a22;
    --track-shadow: #2f3a2a;
    --sky: #cfe3f1;
  }
  * { box-sizing: border-box; margin: 0; padding: 0; }
  html, body { width: 1200px; height: 982px; overflow: hidden; }
  body {
    background: var(--board);
    position: relative;
    font-family: "Roboto Condensed", "Arial Narrow", sans-serif;
  }
  .side-label {
    position: absolute;
    top: 82px;
    font-family: "Open Sans", Arial, sans-serif;
    font-size: 43px;
    color: var(--label);
    letter-spacing: 1px;
    transform: translateX(-50%);
  }
  .side-label--front { left: 310px; }
  .side-label--back { left: 884px; }

  .flyer {
    position: absolute;
    top: 164px;
    width: 515px;
    height: 730px;
    background: var(--paper);
    overflow: hidden;
  }
  .flyer--front { left: 54px; }
  .flyer--back { left: 638px; width: 514px; }

  .stencil { font-family: "Allerta Stencil", Arial, sans-serif; font-weight: 400; }
  .abs { position: absolute; }

  /* Front header */
  .name-tab { left: 35px; top: 5px; width: 122px; height: 26px; background: var(--brand-red); }
  .horse-name {
    color: var(--brand-red);
    font-size: 30px;
    line-height: 33px;
    text-align: center;
    letter-spacing: -0.5px;
    white-space: nowrap;
  }
  .front-name { left: 24px; top: 42px; width: 146px; }
  .pedigree {
    left: 24px; top: 112px; width: 150px;
    text-align: center; font-size: 11px; line-height: 12px; color: var(--ink);
    font-family: "Allerta Stencil", Arial, sans-serif;
    letter-spacing: 0.2px;
  }
  .sale-date { left: 185px; top: 16px; font-size: 16px; color: var(--ink); letter-spacing: 1px; }
  .sale-title { left: 181px; top: 42px; font-size: 21px; line-height: 22px; color: var(--brand-red); letter-spacing: 1px; }
  .lot-info { left: 181px; top: 100px; font-size: 15.5px; line-height: 16px; color: var(--ink); letter-spacing: 0.5px; }

  .photo { position: absolute; }
  .photo--front-hero {
    left: 0; top: 146px; width: 515px; height: 584px;
    background: linear-gradient(180deg, var(--grass-dark) 0%, #3f5a2c 35%, var(--track-shadow) 55%, var(--grass-light) 78%, #8fbe42 100%);
  }

  .race-record {
    left: 38px; top: 146px; width: 115px; height: 519px;
    background: var(--brand-red);
    display: flex; flex-direction: column; align-items: center;
    color: var(--paper);
  }
  .race-record__title { font-size: 17px; margin-top: 24px; letter-spacing: 0.2px; }
  .stat-label { font-size: 18px; color: var(--ink); font-weight: 300; margin-top: 16px; }
  .stat-label--first { margin-top: 24px; }
  .stat-value { font-size: 64px; line-height: 66px; margin-top: 6px; }
  .stat-rule { width: 60px; height: 3px; background: var(--paper); margin-top: 36px; }
  .record-underline { left: 38px; top: 690px; width: 117px; height: 5px; background: var(--paper); }

  .caption {
    position: absolute;
    background: var(--brand-red);
    color: var(--paper);
    text-align: right;
    font-weight: 300;
  }
  .caption--foal {
    left: 216px; top: 535px; width: 299px; height: 148px;
    padding: 8px 14px 0 10px;
    font-size: 16.5px; line-height: 19.2px;
  }

  /* Back header */
  .back-name { left: 14px; top: 22px; width: 140px; text-align: left; font-size: 29px; line-height: 34px; }
  .back-name span { display: block; }
  .back-name .indent { padding-left: 14px; }
  .name-rule { left: 162px; top: 18px; width: 3px; height: 72px; background: var(--brand-red); }
  .profile {
    left: 178px; top: 17px; width: 160px; font-size: 11px; line-height: 12.5px;
    color: var(--ink); letter-spacing: 0.6px; white-space: nowrap;
  }
  .profile p + p { margin-top: 10px; }
  .stats-box {
    left: 343px; top: 0; width: 171px; height: 105px; background: var(--brand-red);
    color: var(--paper);
  }
  .stat { position: absolute; text-align: center; }
  .stat__value { font-size: 30px; line-height: 30px; letter-spacing: 1px; }
  .stat__label { font-size: 11px; letter-spacing: 1px; color: var(--paper); font-family: "Allerta Stencil", Arial, sans-serif; }
  .stat--wins { left: 6px; top: 12px; width: 80px; }
  .stat--places { left: 90px; top: 12px; width: 80px; }
  .stat--roi { left: 45px; top: 58px; width: 80px; }

  .photo--win-main {
    left: 0; top: 105px; width: 514px; height: 315px;
    background: linear-gradient(180deg, #9fc06a 0%, #6a8f3a 28%, #3e4b33 48%, var(--grass-light) 62%, #8cc043 100%);
  }
  .photo--win-small-a {
    left: 0; top: 422px; width: 170px; height: 158px;
    background: linear-gradient(180deg, var(--sky) 0%, #b9cfdc 38%, #5a6b4a 58%, var(--grass-light) 100%);
  }
  .photo--win-small-b {
    left: 0; top: 584px; width: 170px; height: 146px;
    background: linear-gradient(180deg, #3d4e34 0%, #2a2e28 40%, #6e9b38 70%, var(--grass-light) 100%);
  }
  .photo--win-wide {
    left: 174px; top: 422px; width: 340px; height: 308px;
    background: linear-gradient(180deg, #d9e9f5 0%, var(--sky) 38%, #8aa0b0 50%, #6f9c3c 60%, var(--grass-light) 100%);
  }

  .caption--race {
    font-size: 11px; line-height: 13px; padding: 4px 10px 0 6px;
    width: 187px; height: 74px; left: 314px;
  }
  .caption--race-top { top: 312px; }
  .caption--race-bottom { top: 642px; }
  .caption--race-mini {
    left: 51px; width: 115px; height: 43px;
    font-size: 5.6px; line-height: 6.8px; padding: 3px 6px 0 3px;
  }
  .caption--mini-a { top: 530px; }
  .caption--mini-b { top: 678px; }
</style>
</head>
<body>
  <div class="side-label side-label--front">FRONT</div>
  <div class="side-label side-label--back">BACK</div>

  <section class="flyer flyer--front">
    <div class="abs name-tab"></div>
    <h1 class="abs horse-name front-name stencil">VELVET<br>HARBOR</h1>
    <p class="abs pedigree">(by Brightlance, out of Solvara)</p>
    <p class="abs sale-date stencil">30 MAY 2019</p>
    <h2 class="abs sale-title stencil">2019 TANDOR CREST<br>MARE AUCTION</h2>
    <p class="abs lot-info stencil">LOT NUMBER: 1414<br>STABLE: QC 6</p>

    <div class="photo photo--front-hero" role="img" aria-label="Photo of the mare galloping past the finish arch with jockey in red silks"></div>

    <div class="abs race-record">
      <div class="race-record__title">RACE RECORD</div>
      <div class="stat-label stat-label--first">WINS</div>
      <div class="stat-value stencil">07</div>
      <div class="stat-rule"></div>
      <div class="stat-label">SECONDS</div>
      <div class="stat-value stencil">02</div>
      <div class="stat-rule"></div>
      <div class="stat-label">THIRDS</div>
      <div class="stat-value stencil">02</div>
    </div>
    <div class="abs record-underline"></div>

    <p class="caption caption--foal">In foal to Far Meadow, sire of: Stellar Drive (winner of the Group 3 Korimako Stakes by 7.5L), Delve On (winner of the Group 2 Wendhollow Plate), Gale Runner (winner of the Tandor Crest Clockwise Classic), Swift Dart, Nova Lane plus more...</p>
  </section>

  <section class="flyer flyer--back">
    <h1 class="abs horse-name back-name stencil"><span>VELVET</span><span class="indent">HARBOR</span></h1>
    <div class="abs name-rule"></div>
    <div class="abs profile stencil">
      <p>COLOUR: BROWN<br>AGE/SEX: 5YO MARE</p>
      <p>FOAL DATE 10/28/2012<br>SIRE: BRIGHTLANCE<br>DAM: SOLVARA (NZL)</p>
    </div>
    <div class="abs stats-box">
      <div class="stat stat--wins"><div class="stat__value stencil">26%</div><div class="stat__label">WINS</div></div>
      <div class="stat stat--places"><div class="stat__value stencil">90%</div><div class="stat__label">PLACES</div></div>
      <div class="stat stat--roi"><div class="stat__value stencil">41%</div><div class="stat__label">ROI</div></div>
    </div>

    <div class="photo photo--win-main" role="img" aria-label="Photo of the mare winning in front of the big screen at Kestrel Park"></div>
    <p class="caption caption--race caption--race-top">Velvet Harbor wins by 3.5L<br>Class 6 Handicap – 1400m<br>Riverbend Racing Club (Kestrel Park), 21 January 2017</p>

    <div class="photo photo--win-small-a" role="img" aria-label="Photo of the mare winning at Ashdown"></div>
    <p class="caption caption--race-mini caption--mini-a">Velvet Harbor wins by 2.3L<br>Class 4 Handicap – 1400m<br>Riverbend Racing Club (Ashdown), 23 November 2016</p>

    <div class="photo photo--win-small-b" role="img" aria-label="Photo of the mare crossing the line near the grandstand"></div>
    <p class="caption caption--race-mini caption--mini-b">Velvet Harbor wins by 2.8L<br>No More Than One Metro Win Handicap – 1400m<br>Riverbend Racing Club (Kestrel Park), 10 December 2016</p>

    <div class="photo photo--win-wide" role="img" aria-label="Photo of two horses racing down the straight"></div>
    <p class="caption caption--race caption--race-bottom">Velvet Harbor wins by 3.5L<br>Class 6 Handicap – 1400m<br>Riverbend Racing Club (Kestrel Park), 21 January 2017</p>
  </section>
</body>
</html>
```